Resume for higher management position in a mechanical/consultant industries application*

I would like to use this resume for getting a higher position interview possibilities. My skills are multi-cultural negotiation, mechanical industry sales, outsourcing to Asia, ability to manage the agent/reseller system, well team player. multi-language Chinese/English/German specialized. Please make the design, professional, comfortable to read atmosphere.

Target Market(s)

management position, sales related

Font styles to use
Serif
Sans Serif

```html
<!DOCTYPE html>
<html lang="en">
<head>
<meta charset="utf-8">
<title>Wei-Chen Liao – Resume</title>
<link href="https://fonts.googleapis.com/css2?family=Montserrat:wght@300;400;600;700&display=swap" rel="stylesheet">
<style>
:root{
  --accent:#f7a10c;
  --ink:#1a1a1a;
  --text:#3a3a3a;
  --rule:#8a8a8a;
  --paper:#ffffff;
  --hero-dark:#111111;
  --hero-mid:#4a4a4a;
}
*{margin:0;padding:0;box-sizing:border-box}
html,body{width:848px;height:1200px;overflow:hidden;background:var(--paper)}
body{font-family:'Montserrat',Arial,sans-serif;color:var(--text);position:relative;font-weight:300}
.hero{position:absolute;left:0;top:0;width:848px;height:250px;
  background:radial-gradient(ellipse at 60% 40%,#6a6a6a 0%,#3a3a3a 40%,var(--hero-dark) 100%),linear-gradient(90deg,#222,#555,#222)}
.name-frame{position:absolute;left:171px;top:63px;width:508px;height:89px;border:1px solid #e8e8e8}
.name{position:absolute;left:0;width:848px;top:88px;text-align:center;font-size:30px;letter-spacing:14px;color:var(--accent);line-height:1;padding-left:14px}
.name b{font-weight:600}
.name span{font-weight:300}
.tagline{position:absolute;left:0;width:848px;top:170px;text-align:center;font-size:15px;font-weight:600;letter-spacing:6px;color:var(--accent);padding-left:6px}
.section-title{position:absolute;font-size:16px;font-weight:600;letter-spacing:7px;color:var(--accent);line-height:21px}
.rule{position:absolute;height:1px;background:var(--rule)}
.timeline{position:absolute;left:317px;width:1px;background:var(--rule)}
.dot{position:absolute;left:314px;width:7px;height:7px;border-radius:50%;background:var(--accent)}
.contact{position:absolute;left:59px;top:385px;font-size:11px;line-height:14px;color:var(--text)}
.contact li{list-style:none;display:flex;align-items:center;gap:10px}
.contact svg{width:10px;height:10px;flex:none}
.block{position:absolute;font-size:11.2px;line-height:14px;color:var(--text)}
.block h4{font-weight:700;color:var(--ink);font-size:11.2px}
.block p{margin-bottom:14px}
.left{left:59px;width:180px}
.right{left:373px;width:440px}
</style>
</head>
<body>
<header class="hero" role="img" aria-label="Black and white aerial photograph of a downtown skyline"></header>
<div class="name-frame"></div>
<h1 class="name"><b>WEI-CHEN</b> <span>LIAO</span></h1>
<div class="tagline">PROFESSIONAL BUSINESS</div>

<h2 class="section-title" style="left:59px;top:292px">PERSONAL<br>INFORMATION:</h2>
<div class="rule" style="left:59px;top:347px;width:200px"></div>
<ul class="contact">
  <li><svg viewBox="0 0 10 10"><rect x="2.5" y="0.5" width="5" height="9" rx="0.8" fill="none" stroke="#111"/><rect x="2.5" y="7.5" width="5" height="2" fill="#111"/></svg>+xxxxxx</li>
  <li><svg viewBox="0 0 10 10"><rect x="0.5" y="2" width="9" height="6.5" fill="none" stroke="#111"/><path d="M0.5 2 L5 6 L9.5 2" fill="none" stroke="#111"/></svg>xxxxxx@mailbox.com</li>
  <li><svg viewBox="0 0 10 10"><path d="M1 5 L5 1 L9 5 M2 4.5 V9 H8 V4.5" fill="none" stroke="#111"/></svg>xxxxxxxx, Germany</li>
  <li><svg viewBox="0 0 10 10"><rect x="1" y="1" width="8" height="8" fill="#111"/></svg>xxxxxxxxxx</li>
</ul>

<h2 class="section-title" style="left:59px;top:490px">EDUCATION:</h2>
<div class="rule" style="left:59px;top:524px;width:157px"></div>
<div class="block left" style="top:560px">
  <p><strong style="font-weight:700;color:var(--ink)">MBA,<br>Lombard Polytechnic Italy</strong><br>2011-2012</p>
  <p><strong style="font-weight:700;color:var(--ink)">Bachelor<br>Hsin-Ming Technical<br>University</strong><br>2005-2009</p>
</div>
<div class="rule" style="left:59px;top:720px;width:70px"></div>
<div class="block left" style="top:753px;width:190px">
  <h4>Specialties:</h4>
  <p>Great experiences in handling business with Chinese cultural business firms. Multi-national corporation skills( especially in Chinese-speaking market)</p>
  <h4>Multi-language skill:</h4>
  <p>native Chinese speaker/ advanced English/ advanced German</p>
</div>

<div class="timeline" style="top:316px;height:382px"></div>
<div class="timeline" style="top:735px;height:411px"></div>
<div class="dot" style="top:383px"></div>
<div class="dot" style="top:804px"></div>
<div class="dot" style="top:915px"></div>
<div class="dot" style="top:1028px"></div>
<div class="dot" style="top:1097px"></div>

<h2 class="section-title" style="left:373px;top:311px">SUMMARY:</h2>
<div class="rule" style="left:373px;top:345px;width:129px"></div>
<div class="block right" style="top:379px">
  <p style="margin-bottom:28px">Mandarin Chinese/ German/ English speaker, real machining experiences, OEM skills, trade skill, global sourcing</p>
  <p>Currently, I am a “Sales manager Asia” of a top German rotary table company. I am in charge of four countries Japan, China, South Korea and Taiwan with 3 agents, more than 20 salemen team.</p>
  <p>As a director of manufacuturing, I have more than 5 years professional experiences in manufacturing metal components by different CNC-machines. I am capable of coding CNC G,M-code, designing the working path of different parts and managing the whole process.</p>
  <p>I have well-understanding of mechanical outsourcing ecosystem in Taiwan. With deep knowledge of outsourcing metal components to different suppliers in Taiwan.</p>
  <p>Familiar with coordinating with different industrial processes in order to build the final products. (Black oxidizing, Different anodizing, Chemical polishing, Manganese phosphate coating, Heat treatment, and Different grinding methods) Especially love to build prototype in order to get a high profitable potential products. (from zero to one)</p>
</div>

<h2 class="section-title" style="left:373px;top:731px">CURRENTLY:</h2>
<div class="rule" style="left:373px;top:765px;width:157px"></div>
<div class="block right" style="top:800px">
  <h4>Sales Manager Asiaxxxxxxxxxx 2018-now</h4>
  <p>Currently, leading 3 major dealers in Taiwan, Mainland China, South Korea and Japan with more than 20 salesmen team.<br>Rotaris provides rotary tables, trunnions and 2 axis rotary tilt units shall have the best possible technical characteristics in the smallest possible space, is the principle model for our dividing heads -engineering -manufacturing -and assembly.</p>
  <h4>Director of Manufacturing, Kestrel Precision Machinery Company 2012-2017</h4>
  <p>Using CNC turn/mill machine to manufacture any mechanical components as customers want. Also providing great total solutions for our clients.<br>Photos shown in my ProfileNet are my products which are made by CNC turn-milling dual spindles machines(trophy is programmed by CAM).</p>
  <h4>Marketing Analyst, Brightfield Import Mannheim Germany, 2012 Apr- 2012</h4>
  <p>Nov Help Brightfield Import to build their sales/marketing strategy for the new launched product “Glidex” in central Europe.</p>
  <h4>External consultant, Calcestra Group Bergamo Italty, 2011 Oct-2012 Mar</h4>
  <p>To improve the Alpha Suite(ERP system) of Calcestra with re-organized procurement process and new standardized KPIs.</p>
</div>
</body>
</html>
```